Civic Holdwell Business Card

We are looking to design new business cards for our company. We have two office locations and would like to have both full addresses on the card. Each address needs two lines for the building name and street address and a line or two for the city, state and zip code. There should be a place for 2-3 phone numbers. The addresses and phone numbers are at the bottom of this description. We also need a place to put our company website and one email address. Our logo is attached.
We would like the card to be two sided. The back of the card should have a blue background with some part of our logo design on it. We would like the full logo on the front of the card as well. The front of the card should have a white background with the blue logo. We are open to listing our addresses on the front or the back of the card. The person who designed our logo gave us an excellent business card idea that we really liked. I have attached a picture of his business card idea so that we can build off of it.
Addresses:
The Tanner Hall
2184 17th Street NW
Washington, DC 20007
Marlow Crest Tower
410 Dorsen Avenue #2215
Miami, FL 33131
Phone Numbers: (202) 555-0148
(202) 555-0193
Website: www.civicholdwell.example

```html
<!DOCTYPE html>
<html lang="en">
<head>
<meta charset="utf-8">
<title>Civic Holdwell Business Card</title>
<link href="https://fonts.googleapis.com/css2?family=Nunito+Sans:wght@400;700&display=swap" rel="stylesheet">
<style>
  :root {
    --stage: #2a2a2c;
    --brand-blue: #1f2c9a;
    --brand-blue-deep: #17207a;
    --brand-blue-light: #2a3bb4;
    --paper: #ffffff;
    --paper-shade: #e9e9ec;
    --ink-light: #e8ebff;
  }
  * { box-sizing: border-box; margin: 0; padding: 0; }
  html, body { width: 1200px; height: 900px; overflow: hidden; }
  body {
    background: var(--stage);
    font-family: "Nunito Sans", sans-serif;
    display: flex;
    flex-direction: column;
    align-items: center;
    justify-content: center;
    gap: 40px;
  }
  .card {
    position: relative;
    width: 700px;
    height: 400px;
    overflow: hidden;
    box-shadow: 0 10px 30px rgba(0,0,0,0.45);
  }
  .card-art { position: absolute; inset: 0; }

  /* Front */
  .card-front { background: var(--brand-blue); }
  .brand-lockup {
    position: absolute;
    left: 44px;
    top: 110px;
    display: flex;
    align-items: center;
    gap: 12px;
  }
  .brand-mark {
    width: 44px;
    height: 44px;
    background: var(--brand-blue);
    border-radius: 6px;
  }
  .brand-name {
    font-size: 38px;
    font-weight: 400;
    letter-spacing: 1px;
    text-transform: uppercase;
    color: var(--brand-blue);
    line-height: 1;
  }
  .office {
    position: absolute;
    font-style: normal;
    color: var(--ink-light);
    font-size: 14px;
    line-height: 19px;
  }
  .office-name { font-weight: 700; color: var(--paper); }
  .office-dc { left: 44px; top: 280px; }
  .office-miami { left: 448px; top: 212px; }

  /* Back */
  .card-back {
    background: linear-gradient(160deg, var(--brand-blue-light) 0%, var(--brand-blue) 55%, var(--brand-blue-deep) 100%);
  }
  .back-emblem {
    position: absolute;
    left: 70px;
    top: 60px;
    width: 280px;
    height: 280px;
    border-radius: 50%;
    background: rgba(255,255,255,0.06);
  }
  .back-lockup {
    position: absolute;
    right: 48px;
    top: 168px;
    text-align: right;
  }
  .back-lockup .brand-name { color: var(--paper); font-size: 34px; }
  .back-web {
    margin-top: 10px;
    font-size: 14px;
    color: var(--ink-light);
    letter-spacing: 0.3px;
  }
</style>
</head>
<body>

  <section class="card card-front" aria-label="Business card front">
    <svg class="card-art" viewBox="0 0 700 400" width="700" height="400" aria-hidden="true">
      <defs>
        <linearGradient id="paperGrad" x1="0" y1="0" x2="0" y2="1">
          <stop offset="0" stop-color="#ffffff"/>
          <stop offset="1" stop-color="#e9e9ec"/>
        </linearGradient>
      </defs>
      <path d="M0,0 H700 V90 Q430,240 0,268 Z" fill="url(#paperGrad)"/>
      <path d="M300,254 Q520,228 672,108 Q540,238 300,254 Z" fill="#ffffff" opacity="0.25"/>
    </svg>

    <div class="brand-lockup">
      <span class="brand-mark"></span>
      <span class="brand-name">Civic Holdwell</span>
    </div>

    <address class="office office-dc">
      <div class="office-name">The Tanner Hall</div>
      <div>2184 17th Street NW</div>
      <div>Washington, DC 20007</div>
      <div>P: (202) 555-0148</div>
      <div>P: (202) 555-0193</div>
      <div>info1@civicholdwell.example</div>
    </address>

    <address class="office office-miami">
      <div class="office-name">Marlow Crest Tower</div>
      <div>410 Dorsen Avenue #2215</div>
      <div>Miami, FL 33131</div>
      <div>P: (202) 555-0148</div>
      <div>P: (202) 555-0193</div>
      <div>info2@civicholdwell.example</div>
    </address>
  </section>

  <section class="card card-back" aria-label="Business card back">
    <div class="back-emblem" role="img" aria-label="Faint brand emblem decoration"></div>
    <div class="back-lockup">
      <div class="brand-name">Civic Holdwell</div>
      <div class="back-web">www.civicholdwell.example</div>
    </div>
  </section>

</body>
</html>
```